Create a backdrop for a trade show booth!

We are looking for a design to put on a 10'X10' trade show booth for our company: Dalvick Pulse Clean.

Please see website: www.dalvickpulseclean.com

It Company

```html
<!DOCTYPE html>
<html lang="en">
<head>
<meta charset="utf-8">
<title>Dalvick Pulse Clean — Trade Show Backdrop</title>
<link rel="stylesheet" href="https://fonts.googleapis.com/css2?family=Cinzel:wght@600&display=swap">
<style>
  :root {
    --page-bg: #eeeeee;
    --backdrop-blue: #1616e6;
    --brand-white: #ffffff;
    --brand-ice: #5ff0e0;
  }
  * { margin: 0; padding: 0; box-sizing: border-box; }
  html, body {
    width: 785px;
    height: 1200px;
    overflow: hidden;
    background: var(--page-bg);
  }
  .backdrop {
    position: absolute;
    left: 42px;
    top: 250px;
    width: 700px;
    height: 700px;
    background: var(--backdrop-blue);
    overflow: hidden;
    font-family: "Cinzel", Georgia, serif;
    font-weight: 600;
  }
  .repeat-pattern {
    position: absolute;
    inset: 0;
    padding-top: 6px;
  }
  .pattern-row {
    display: flex;
    height: 46px;
    align-items: center;
    white-space: nowrap;
  }
  .pattern-row--offset { margin-left: -50px; }
  .tile {
    flex: 0 0 100px;
    display: flex;
    align-items: center;
    gap: 4px;
    padding-left: 6px;
  }
  .tile-dot {
    width: 18px;
    height: 18px;
    border-radius: 50%;
    background: var(--brand-ice);
    flex: none;
  }
  .tile-name {
    color: var(--brand-white);
    font-size: 8.5px;
    line-height: 1.05;
    letter-spacing: 0.04em;
  }
  .feature-panel {
    position: absolute;
    left: 190px;
    top: 276px;
    width: 320px;
    height: 186px;
    background: var(--backdrop-blue);
    display: flex;
    flex-direction: column;
    align-items: center;
    justify-content: center;
    gap: 10px;
  }
  .feature-mark {
    width: 92px;
    height: 92px;
    border-radius: 50%;
    background: var(--brand-ice);
  }
  .feature-name {
    color: var(--brand-white);
    font-size: 30px;
    letter-spacing: 0.12em;
    line-height: 1;
    text-align: center;
  }
</style>
</head>
<body>
<main class="backdrop">
  <div class="repeat-pattern" aria-hidden="true">
    <div class="pattern-row">
      <div class="tile"><span class="tile-dot"></span><span class="tile-name">DALVICK<br>PULSE CLEAN</span></div>
      <div class="tile"><span class="tile-dot"></span><span class="tile-name">DALVICK<br>PULSE CLEAN</span></div>
      <div class="tile"><span class="tile-dot"></span><span class="tile-name">DALVICK<br>PULSE CLEAN</span></div>
      <div class="tile"><span class="tile-dot"></span><span class="tile-name">DALVICK<br>PULSE CLEAN</span></div>
      <div class="tile"><span class="tile-dot"></span><span class="tile-name">DALVICK<br>PULSE CLEAN</span></div>
      <div class="tile"><span class="tile-dot"></span><span class="tile-name">DALVICK<br>PULSE CLEAN</span></div>
      <div class="tile"><span class="tile-dot"></span><span class="tile-name">DALVICK<br>PULSE CLEAN</span></div>
    </div>
    <div class="pattern-row pattern-row--offset">
      <div class="tile"><span class="tile-dot"></span><span class="tile-name">DALVICK<br>PULSE CLEAN</span></div>
      <div class="tile"><span class="tile-dot"></span><span class="tile-name">DALVICK<br>PULSE CLEAN</span></div>
      <div class="tile"><span class="tile-dot"></span><span class="tile-name">DALVICK<br>PULSE CLEAN</span></div>
      <div class="tile"><span class="tile-dot"></span><span class="tile-name">DALVICK<br>PULSE CLEAN</span></div>
      <div class="tile"><span class="tile-dot"></span><span class="tile-name">DALVICK<br>PULSE CLEAN</span></div>
      <div class="tile"><span class="tile-dot"></span><span class="tile-name">DALVICK<br>PULSE CLEAN</span></div>
      <div class="tile"><span class="tile-dot"></span><span class="tile-name">DALVICK<br>PULSE CLEAN</span></div>
      <div class="tile"><span class="tile-dot"></span><span class="tile-name">DALVICK<br>PULSE CLEAN</span></div>
    </div>
    <div class="pattern-row">
      <div class="tile"><span class="tile-dot"></span><span class="tile-name">DALVICK<br>PULSE CLEAN</span></div>
      <div class="tile"><span class="tile-dot"></span><span class="tile-name">DALVICK<br>PULSE CLEAN</span></div>
      <div class="tile"><span class="tile-dot"></span><span class="tile-name">DALVICK<br>PULSE CLEAN</span></div>
      <div class="tile"><span class="tile-dot"></span><span class="tile-name">DALVICK<br>PULSE CLEAN</span></div>
      <div class="tile"><span class="tile-dot"></span><span class="tile-name">DALVICK<br>PULSE CLEAN</span></div>
      <div class="tile"><span class="tile-dot"></span><span class="tile-name">DALVICK<br>PULSE CLEAN</span></div>
      <div class="tile"><span class="tile-dot"></span><span class="tile-name">DALVICK<br>PULSE CLEAN</span></div>
    </div>
    <div class="pattern-row pattern-row--offset">
      <div class="tile"><span class="tile-dot"></span><span class="tile-name">DALVICK<br>PULSE CLEAN</span></div>
      <div class="tile"><span class="tile-dot"></span><span class="tile-name">DALVICK<br>PULSE CLEAN</span></div>
      <div class="tile"><span class="tile-dot"></span><span class="tile-name">DALVICK<br>PULSE CLEAN</span></div>
      <div class="tile"><span class="tile-dot"></span><span class="tile-name">DALVICK<br>PULSE CLEAN</span></div>
      <div class="tile"><span class="tile-dot"></span><span class="tile-name">DALVICK<br>PULSE CLEAN</span></div>
      <div class="tile"><span class="tile-dot"></span><span class="tile-name">DALVICK<br>PULSE CLEAN</span></div>
      <div class="tile"><span class="tile-dot"></span><span class="tile-name">DALVICK<br>PULSE CLEAN</span></div>
      <div class="tile"><span class="tile-dot"></span><span class="tile-name">DALVICK<br>PULSE CLEAN</span></div>
    </div>
    <div class="pattern-row">
      <div class="tile"><span class="tile-dot"></span><span class="tile-name">DALVICK<br>PULSE CLEAN</span></div>
      <div class="tile"><span class="tile-dot"></span><span class="tile-name">DALVICK<br>PULSE CLEAN</span></div>
      <div class="tile"><span class="tile-dot"></span><span class="tile-name">DALVICK<br>PULSE CLEAN</span></div>
      <div class="tile"><span class="tile-dot"></span><span class="tile-name">DALVICK<br>PULSE CLEAN</span></div>
      <div class="tile"><span class="tile-dot"></span><span class="tile-name">DALVICK<br>PULSE CLEAN</span></div>
      <div class="tile"><span class="tile-dot"></span><span class="tile-name">DALVICK<br>PULSE CLEAN</span></div>
      <div class="tile"><span class="tile-dot"></span><span class="tile-name">DALVICK<br>PULSE CLEAN</span></div>
    </div>
    <div class="pattern-row pattern-row--offset">
      <div class="tile"><span class="tile-dot"></span><span class="tile-name">DALVICK<br>PULSE CLEAN</span></div>
      <div class="tile"><span class="tile-dot"></span><span class="tile-name">DALVICK<br>PULSE CLEAN</span></div>
      <div class="tile"><span class="tile-dot"></span><span class="tile-name">DALVICK<br>PULSE CLEAN</span></div>
      <div class="tile"><span class="tile-dot"></span><span class="tile-name">DALVICK<br>PULSE CLEAN</span></div>
      <div class="tile"><span class="tile-dot"></span><span class="tile-name">DALVICK<br>PULSE CLEAN</span></div>
      <div class="tile"><span class="tile-dot"></span><span class="tile-name">DALVICK<br>PULSE CLEAN</span></div>
      <div class="tile"><span class="tile-dot"></span><span class="tile-name">DALVICK<br>PULSE CLEAN</span></div>
      <div class="tile"><span class="tile-dot"></span><span class="tile-name">DALVICK<br>PULSE CLEAN</span></div>
    </div>
    <div class="pattern-row">
      <div class="tile"><span class="tile-dot"></span><span class="tile-name">DALVICK<br>PULSE CLEAN</span></div>
      <div class="tile"><span class="tile-dot"></span><span class="tile-name">DALVICK<br>PULSE CLEAN</span></div>
      <div class="tile"><span class="tile-dot"></span><span class="tile-name">DALVICK<br>PULSE CLEAN</span></div>
      <div class="tile"><span class="tile-dot"></span><span class="tile-name">DALVICK<br>PULSE CLEAN</span></div>
      <div class="tile"><span class="tile-dot"></span><span class="tile-name">DALVICK<br>PULSE CLEAN</span></div>
      <div class="tile"><span class="tile-dot"></span><span class="tile-name">DALVICK<br>PULSE CLEAN</span></div>
      <div class="tile"><span class="tile-dot"></span><span class="tile-name">DALVICK<br>PULSE CLEAN</span></div>
    </div>
    <div class="pattern-row pattern-row--offset">
      <div class="tile"><span class="tile-dot"></span><span class="tile-name">DALVICK<br>PULSE CLEAN</span></div>
      <div class="tile"><span class="tile-dot"></span><span class="tile-name">DALVICK<br>PULSE CLEAN</span></div>
      <div class="tile"><span class="tile-dot"></span><span class="tile-name">DALVICK<br>PULSE CLEAN</span></div>
      <div class="tile"><span class="tile-dot"></span><span class="tile-name">DALVICK<br>PULSE CLEAN</span></div>
      <div class="tile"><span class="tile-dot"></span><span class="tile-name">DALVICK<br>PULSE CLEAN</span></div>
      <div class="tile"><span class="tile-dot"></span><span class="tile-name">DALVICK<br>PULSE CLEAN</span></div>
      <div class="tile"><span class="tile-dot"></span><span class="tile-name">DALVICK<br>PULSE CLEAN</span></div>
      <div class="tile"><span class="tile-dot"></span><span class="tile-name">DALVICK<br>PULSE CLEAN</span></div>
    </div>
    <div class="pattern-row">
      <div class="tile"><span class="tile-dot"></span><span class="tile-name">DALVICK<br>PULSE CLEAN</span></div>
      <div class="tile"><span class="tile-dot"></span><span class="tile-name">DALVICK<br>PULSE CLEAN</span></div>
      <div class="tile"><span class="tile-dot"></span><span class="tile-name">DALVICK<br>PULSE CLEAN</span></div>
      <div class="tile"><span class="tile-dot"></span><span class="tile-name">DALVICK<br>PULSE CLEAN</span></div>
      <div class="tile"><span class="tile-dot"></span><span class="tile-name">DALVICK<br>PULSE CLEAN</span></div>
      <div class="tile"><span class="tile-dot"></span><span class="tile-name">DALVICK<br>PULSE CLEAN</span></div>
      <div class="tile"><span class="tile-dot"></span><span class="tile-name">DALVICK<br>PULSE CLEAN</span></div>
    </div>
    <div class="pattern-row pattern-row--offset">
      <div class="tile"><span class="tile-dot"></span><span class="tile-name">DALVICK<br>PULSE CLEAN</span></div>
      <div class="tile"><span class="tile-dot"></span><span class="tile-name">DALVICK<br>PULSE CLEAN</span></div>
      <div class="tile"><span class="tile-dot"></span><span class="tile-name">DALVICK<br>PULSE CLEAN</span></div>
      <div class="tile"><span class="tile-dot"></span><span class="tile-name">DALVICK<br>PULSE CLEAN</span></div>
      <div class="tile"><span class="tile-dot"></span><span class="tile-name">DALVICK<br>PULSE CLEAN</span></div>
      <div class="tile"><span class="tile-dot"></span><span class="tile-name">DALVICK<br>PULSE CLEAN</span></div>
      <div class="tile"><span class="tile-dot"></span><span class="tile-name">DALVICK<br>PULSE CLEAN</span></div>
      <div class="tile"><span class="tile-dot"></span><span class="tile-name">DALVICK<br>PULSE CLEAN</span></div>
    </div>
    <div class="pattern-row">
      <div class="tile"><span class="tile-dot"></span><span class="tile-name">DALVICK<br>PULSE CLEAN</span></div>
      <div class="tile"><span class="tile-dot"></span><span class="tile-name">DALVICK<br>PULSE CLEAN</span></div>
      <div class="tile"><span class="tile-dot"></span><span class="tile-name">DALVICK<br>PULSE CLEAN</span></div>
      <div class="tile"><span class="tile-dot"></span><span class="tile-name">DALVICK<br>PULSE CLEAN</span></div>
      <div class="tile"><span class="tile-dot"></span><span class="tile-name">DALVICK<br>PULSE CLEAN</span></div>
      <div class="tile"><span class="tile-dot"></span><span class="tile-name">DALVICK<br>PULSE CLEAN</span></div>
      <div class="tile"><span class="tile-dot"></span><span class="tile-name">DALVICK<br>PULSE CLEAN</span></div>
    </div>
    <div class="pattern-row pattern-row--offset">
      <div class="tile"><span class="tile-dot"></span><span class="tile-name">DALVICK<br>PULSE CLEAN</span></div>
      <div class="tile"><span class="tile-dot"></span><span class="tile-name">DALVICK<br>PULSE CLEAN</span></div>
      <div class="tile"><span class="tile-dot"></span><span class="tile-name">DALVICK<br>PULSE CLEAN</span></div>
      <div class="tile"><span class="tile-dot"></span><span class="tile-name">DALVICK<br>PULSE CLEAN</span></div>
      <div class="tile"><span class="tile-dot"></span><span class="tile-name">DALVICK<br>PULSE CLEAN</span></div>
      <div class="tile"><span class="tile-dot"></span><span class="tile-name">DALVICK<br>PULSE CLEAN</span></div>
      <div class="tile"><span class="tile-dot"></span><span class="tile-name">DALVICK<br>PULSE CLEAN</span></div>
      <div class="tile"><span class="tile-dot"></span><span class="tile-name">DALVICK<br>PULSE CLEAN</span></div>
    </div>
    <div class="pattern-row">
      <div class="tile"><span class="tile-dot"></span><span class="tile-name">DALVICK<br>PULSE CLEAN</span></div>
      <div class="tile"><span class="tile-dot"></span><span class="tile-name">DALVICK<br>PULSE CLEAN</span></div>
      <div class="tile"><span class="tile-dot"></span><span class="tile-name">DALVICK<br>PULSE CLEAN</span></div>
      <div class="tile"><span class="tile-dot"></span><span class="tile-name">DALVICK<br>PULSE CLEAN</span></div>
      <div class="tile"><span class="tile-dot"></span><span class="tile-name">DALVICK<br>PULSE CLEAN</span></div>
      <div class="tile"><span class="tile-dot"></span><span class="tile-name">DALVICK<br>PULSE CLEAN</span></div>
      <div class="tile"><span class="tile-dot"></span><span class="tile-name">DALVICK<br>PULSE CLEAN</span></div>
    </div>
    <div class="pattern-row pattern-row--offset">
      <div class="tile"><span class="tile-dot"></span><span class="tile-name">DALVICK<br>PULSE CLEAN</span></div>
      <div class="tile"><span class="tile-dot"></span><span class="tile-name">DALVICK<br>PULSE CLEAN</span></div>
      <div class="tile"><span class="tile-dot"></span><span class="tile-name">DALVICK<br>PULSE CLEAN</span></div>
      <div class="tile"><span class="tile-dot"></span><span class="tile-name">DALVICK<br>PULSE CLEAN</span></div>
      <div class="tile"><span class="tile-dot"></span><span class="tile-name">DALVICK<br>PULSE CLEAN</span></div>
      <div class="tile"><span class="tile-dot"></span><span class="tile-name">DALVICK<br>PULSE CLEAN</span></div>
      <div class="tile"><span class="tile-dot"></span><span class="tile-name">DALVICK<br>PULSE CLEAN</span></div>
      <div class="tile"><span class="tile-dot"></span><span class="tile-name">DALVICK<br>PULSE CLEAN</span></div>
    </div>
    <div class="pattern-row">
      <div class="tile"><span class="tile-dot"></span><span class="tile-name">DALVICK<br>PULSE CLEAN</span></div>
      <div class="tile"><span class="tile-dot"></span><span class="tile-name">DALVICK<br>PULSE CLEAN</span></div>
      <div class="tile"><span class="tile-dot"></span><span class="tile-name">DALVICK<br>PULSE CLEAN</span></div>
      <div class="tile"><span class="tile-dot"></span><span class="tile-name">DALVICK<br>PULSE CLEAN</span></div>
      <div class="tile"><span class="tile-dot"></span><span class="tile-name">DALVICK<br>PULSE CLEAN</span></div>
      <div class="tile"><span class="tile-dot"></span><span class="tile-name">DALVICK<br>PULSE CLEAN</span></div>
      <div class="tile"><span class="tile-dot"></span><span class="tile-name">DALVICK<br>PULSE CLEAN</span></div>
    </div>
  </div>

  <section class="feature-panel">
    <span class="feature-mark" aria-hidden="true"></span>
    <h1 class="feature-name">DALVICK<br>PULSE CLEAN</h1>
  </section>
</main>
</body>
</html>
```